New Innovative Counselling and psychotherapy Service needs Business Card design

Keep it simple and professional. On one side, just company name and logo (perhaps in all blue) and maybe a tag line.

On other side (all white) my name and Qualifications in centre

Industry/Entity Type

Health And Wellness

Contact Information for Business Card

Derek Hollis
Counsellor & Psychotherapist
BSc (Psychol.), BA, Dip. (Couns. & Psych.), PG.Cert (CBT), ADLnR, ESGW

I will also require Mobile no, Email and web site address of which I'll pass on to final designer.

Font styles to use
Sans Serif

Requirements
Must have
• My Logo Only and please use the colours in logo that is in it.
Should not have
• Any other images

```html
<!DOCTYPE html>
<html lang="en">
<head>
<meta charset="utf-8">
<title>Steady Path – Business Card</title>
<link rel="stylesheet" href="https://fonts.googleapis.com/css2?family=Roboto:wght@400;500;700&display=swap">
<style>
  :root {
    --page-bg: #e9e7e3;
    --card-bg: #f6f6f4;
    --ink-dark: #3a3d40;
    --ink-body: #3b3e42;
    --brand-blue: #3b9fd1;
    --brand-green: #7bbf4a;
    --icon-teal: #2f9c8c;
  }
  * { margin: 0; padding: 0; box-sizing: border-box; }
  html, body {
    width: 1200px;
    height: 1054px;
    overflow: hidden;
    background: var(--page-bg);
    font-family: "Roboto", Arial, sans-serif;
  }
  .card {
    position: absolute;
    left: 100px;
    top: 227px;
    width: 1000px;
    height: 603px;
    background: var(--card-bg);
    box-shadow: 0 10px 30px rgba(0,0,0,0.12);
    overflow: hidden;
  }
  .brand {
    position: absolute;
    left: 51px;
    top: 55px;
    display: flex;
    align-items: center;
  }
  .brand-dot {
    width: 128px;
    height: 128px;
    border-radius: 50%;
    background: var(--brand-blue);
  }
  .brand-name {
    margin-left: 52px;
    font-size: 76px;
    font-weight: 400;
    color: var(--ink-dark);
    letter-spacing: -0.5px;
  }
  .person {
    position: absolute;
    left: 61px;
    top: 302px;
    color: var(--ink-body);
  }
  .person-name {
    font-size: 37px;
    font-weight: 700;
    color: var(--brand-blue);
    line-height: 44px;
  }
  .person-role,
  .person-quals {
    font-size: 23px;
    line-height: 31px;
  }
  .contacts {
    position: absolute;
    left: 61px;
    top: 449px;
    list-style: none;
  }
  .contact-item {
    display: flex;
    align-items: center;
    height: 37.5px;
    font-size: 25px;
    color: var(--ink-body);
  }
  .contact-icon {
    width: 22px;
    height: 22px;
    margin-right: 29px;
  }
  .accent-bar {
    position: absolute;
    left: 0;
    bottom: 0;
    width: 100%;
    height: 16px;
    display: flex;
  }
  .accent-blue { flex: 1; background: var(--brand-blue); }
  .accent-green { flex: 1; background: var(--brand-green); }
</style>
</head>
<body>
  <div class="card">
    <div class="brand">
      <div class="brand-dot"></div>
      <div class="brand-name">Steady Path</div>
    </div>

    <div class="person">
      <div class="person-name">Derek Hollis</div>
      <div class="person-role">Counsellor &amp; Psychotherapist</div>
      <div class="person-quals">BSc (Psychol.), BA, Dip. (Couns. &amp; Psych.), PG.Cert (CBT), ADLnR, ESGW</div>
    </div>

    <ul class="contacts">
      <li class="contact-item">
        <svg class="contact-icon" viewBox="0 0 24 24" aria-hidden="true">
          <path d="M3 9c0-3 4-5 9-5s9 2 9 5v2h-5V9c-1-.6-2.4-1-4-1s-3 .4-4 1v2H3z" fill="var(--icon-teal)"/>
          <path d="M6 13h12l2 7H4z" fill="var(--icon-teal)"/>
          <circle cx="12" cy="16.5" r="2" fill="var(--card-bg)"/>
        </svg>
        2468 135 7092
      </li>
      <li class="contact-item">
        <svg class="contact-icon" viewBox="0 0 24 24" aria-hidden="true">
          <rect x="2" y="5" width="20" height="14" fill="var(--brand-green)"/>
          <path d="M2 5l10 8 10-8" fill="none" stroke="var(--card-bg)" stroke-width="1.6"/>
        </svg>
        derek.h@SteadyPath.com
      </li>
      <li class="contact-item">
        <svg class="contact-icon" viewBox="0 0 24 24" aria-hidden="true">
          <circle cx="12" cy="12" r="10" fill="var(--brand-green)"/>
          <g fill="none" stroke="var(--card-bg)" stroke-width="1.3">
            <ellipse cx="12" cy="12" rx="4" ry="10"/>
            <line x1="2" y1="12" x2="22" y2="12"/>
            <line x1="12" y1="2" x2="12" y2="22"/>
          </g>
        </svg>
        www.SteadyPath.com
      </li>
    </ul>

    <div class="accent-bar">
      <div class="accent-blue"></div>
      <div class="accent-green"></div>
    </div>
  </div>
</body>
</html>
```